Create a bold and border around my logo to make it pop and sign graphic design

I would like someone to create a sign graphic design so I can use on the side of my trucks and put on yard signs. I would to remove a lot of the white and add more of the orange and blue to give it more pop when cars drive past. I would like the services to be removed and for you to leave space for a mobile number that i would add later. I don’t want my logo changed at all. I just want colour and design to be added to the background so i can use it in signage. Same colour as on the sign

```html
<!DOCTYPE html>
<html lang="en">
<head>
<meta charset="utf-8">
<title>Elmwood Markings – Vehicle &amp; Yard Sign</title>
<link rel="stylesheet" href="https://fonts.googleapis.com/css2?family=Montserrat:wght@700&display=swap">
<style>
  :root {
    --brand-orange: #e6731f;
    --brand-blue: #3e5aa8;
    --paper: #ffffff;
  }
  html, body {
    margin: 0;
    padding: 0;
    width: 1200px;
    height: 1200px;
    overflow: hidden;
    background: var(--paper);
  }
  .sign {
    display: block;
    width: 1200px;
    height: 1200px;
  }
  .sign-text {
    font-family: "Montserrat", Arial, sans-serif;
    font-weight: 700;
    fill: var(--paper);
  }
  .panel-orange, .phone-pill { fill: var(--brand-orange); }
  .panel-blue { fill: var(--brand-blue); }
  .logo-disc { fill: var(--paper); }
  .phone-icon { fill: var(--brand-blue); stroke: var(--paper); stroke-width: 2; }
</style>
</head>
<body>
<svg class="sign" viewBox="0 0 1200 1200" xmlns="http://www.w3.org/2000/svg" role="img" aria-label="Elmwood Markings sign with mobile number">
  <!-- background panels -->
  <rect class="panel-orange" x="172" y="402" width="240" height="403"/>
  <rect class="panel-blue" x="412" y="402" width="623" height="403"/>

  <!-- logo area -->
  <circle class="logo-disc" cx="412" cy="603" r="203" role="img" aria-label="Client logo emblem"/>

  <!-- business name -->
  <text class="sign-text" x="620" y="603" font-size="128" textLength="371" lengthAdjust="spacingAndGlyphs">ELMWOOD</text>
  <text class="sign-text" x="641" y="657" font-size="52" textLength="334" lengthAdjust="spacingAndGlyphs">MARKINGS</text>

  <!-- phone number -->
  <rect class="phone-pill" x="676" y="709" width="315" height="52" rx="12"/>
  <g class="phone-icon" transform="rotate(-20 708 735)">
    <rect x="697" y="712" width="22" height="46" rx="3"/>
  </g>
  <text class="sign-text" x="733" y="749" font-size="36" textLength="240" lengthAdjust="spacingAndGlyphs">0215550147</text>
</svg>
</body>
</html>
```